MEDICAL CLINIC LETTERHEAD

Design is a letterhead for a non-profit medical center. The name of the clinic is VYRLOTEN Community Health Center. Although the full name must be included, the community health center part is more of a description and should be less visible - i attached an example of what I mean by that (ATTACHED IMAGE IS AN EXAMPLE OF FONT SIZES NOT A DESIGN IDEA). Please design something modern, cool looking and unique because I can always download free templates.
Phone, email, website and etc will be added later.

Industry/Entity Type

MEDICAL

```html
<!DOCTYPE html>
<html lang="en">
<head>
<meta charset="utf-8">
<title>VYRLOTEN Community Health Center – Letterhead</title>
<link href="https://fonts.googleapis.com/css2?family=Lato:wght@400;700&display=swap" rel="stylesheet">
<style>
  :root {
    --backdrop: #000000;
    --paper: #ffffff;
    --navy: #0b2f5b;
    --accent: #f29a1f;
    --body-text: #8a8a8a;
    --footer-text: #3f3f3f;
    --rule: #555555;
  }
  * { margin: 0; padding: 0; box-sizing: border-box; }
  html, body {
    width: 960px; height: 1200px; overflow: hidden;
    background: var(--backdrop);
    font-family: "Lato", sans-serif;
  }
  .letterhead {
    position: absolute; left: 50px; top: 44px;
    width: 859px; height: 1112px;
    background: var(--paper);
  }
  .brand {
    position: absolute; left: 0; right: 0; top: 110px;
    text-align: center; color: var(--navy); font-weight: 700;
  }
  .brand-dot {
    display: block; margin: 0 auto 14px;
    width: 18px; height: 18px; border-radius: 50%;
    background: var(--accent);
  }
  .brand-name { font-size: 44px; line-height: 44px; letter-spacing: -0.5px; }
  .brand-desc { font-size: 14.5px; line-height: 18px; margin-top: 2px; text-transform: uppercase; }
  .salutation {
    position: absolute; left: 74px; top: 284px;
    font-size: 16px; color: var(--body-text);
  }
  .letter-body {
    position: absolute; left: 55px; top: 353px; width: 749px;
    font-size: 15.3px; line-height: 20.2px; color: var(--body-text);
    text-align: justify;
  }
  .letter-body p + p { margin-top: 20.2px; }
  .letter-body p:first-child { text-indent: 50px; }
  .contact {
    position: absolute; top: 1022px;
    font-size: 13px; line-height: 17px; color: var(--footer-text);
  }
  .contact-row { display: flex; align-items: center; gap: 8px; }
  .contact svg { width: 11px; height: 11px; fill: var(--footer-text); flex: none; }
  .contact-address { left: 60px; top: 1037px; display: flex; gap: 9px; align-items: center; }
  .contact-address svg { width: 10px; height: 16px; }
  .contact-phone { left: 394px; }
  .contact-online { left: 641px; }
  .contact-phone .contact-row + .contact-row { margin-top: 2px; }
  .divider {
    position: absolute; top: 1022px; width: 1px; height: 50px;
    background: var(--rule);
  }
  .divider-one { left: 303px; }
  .divider-two { left: 588px; }
  .footer-band {
    position: absolute; left: 0; right: 0; bottom: 0; height: 30px;
    background: var(--navy);
  }
</style>
</head>
<body>
<main class="letterhead">
  <header class="brand">
    <span class="brand-dot"></span>
    <div class="brand-name">VYRLOTEN</div>
    <div class="brand-desc">Community Health Center</div>
  </header>

  <p class="salutation">Dear Sir</p>

  <section class="letter-body">
    <p>Lorem ipsum dolor sit amet, consectetur adipiscing elit. Integer eu odio mattis, pulvinar turpis quis, faucibus nisl. Proin feugiat, erat vitae cursus pharetra, enim est semper ligula, in malesuada orci nisl et diam. Etiam elementum metus ac fringilla vulputate. Etiam mattis ligula sed ante mollis bibendum. Orci varius natoque penatibus et magnis dis parturient montes, nascetur ridiculus mus.</p>
    <p>Ut nibh augue, blandit ac orci ac, rutrum congue enim. Suspendisse gravida vulputate felis, quis interdum orci tincidunt quis. Praesent imperdiet maximus neque. Mauris ut dui enim. Nullam at efficitur elit. Donec ante ipsum, fermentum at lectus vel, blandit vulputate ante. Proin luctus suscipit diam id vestibulum. Morbi malesuada id mauris eget ullamcorper.</p>
    <p>Donec varius orci purus, vitae aliquam libero volutpat id. Integer sed imperdiet libero. Aliquam accumsan, risus sit amet ornare consectetur, turpis felis dictum justo, non rhoncus mauris dui sed velit. Pellentesque habitant morbi tristique senectus et netus et malesuada fames ac turpis egestas. Pellentesque tincidunt vitae ligula nec imperdiet. Donec sed congue enim. Nullam elementum faucibus nulla nec vestibulum. Sed at tempor ligula. In quis vulputate nunc. Integer at gravida lacus, ac tristique risus. Sed at vulputate nulla.</p>
    <p>Praesent blandit nunc eu efficitur commodo. In tempor nisi ex, vel venenatis ante vestibulum a. Duis vestibulum nibh a erat sagittis, nec euismod lorem varius. Nam ultricies turpis sed justo sollicitudin volutpat. Morbi sed mollis eros. Sed quis tortor id enim vehicula porttitor. Curabitur non aliquam ex. Phasellus dignissim fermentum elit, at finibus ligula mattis eget.</p>
  </section>

  <footer>
    <div class="contact contact-address">
      <svg viewBox="0 0 10 16" aria-hidden="true"><path d="M5 0a5 5 0 0 0-5 5c0 3.5 5 11 5 11s5-7.5 5-11a5 5 0 0 0-5-5zm0 7a2 2 0 1 1 0-4 2 2 0 0 1 0 4z"/></svg>
      <div>suit # 00, Lorem ipsum<br>Lorem Lorem ipsum</div>
    </div>
    <span class="divider divider-one"></span>
    <div class="contact contact-phone">
      <div class="contact-row">
        <svg viewBox="0 0 24 24" aria-hidden="true"><path d="M6.6 10.8a15.2 15.2 0 0 0 6.6 6.6l2.2-2.2a1 1 0 0 1 1-.25 11.4 11.4 0 0 0 3.6.57 1 1 0 0 1 1 1V20a1 1 0 0 1-1 1A17 17 0 0 1 3 4a1 1 0 0 1 1-1h3.5a1 1 0 0 1 1 1c0 1.25.2 2.45.57 3.57a1 1 0 0 1-.25 1z"/></svg>
        <span>000-000-0000</span>
      </div>
      <div class="contact-row">
        <svg viewBox="0 0 24 24" aria-hidden="true"><path d="M6.6 10.8a15.2 15.2 0 0 0 6.6 6.6l2.2-2.2a1 1 0 0 1 1-.25 11.4 11.4 0 0 0 3.6.57 1 1 0 0 1 1 1V20a1 1 0 0 1-1 1A17 17 0 0 1 3 4a1 1 0 0 1 1-1h3.5a1 1 0 0 1 1 1c0 1.25.2 2.45.57 3.57a1 1 0 0 1-.25 1z"/></svg>
        <span>000-000-0000</span>
      </div>
    </div>
    <span class="divider divider-two"></span>
    <div class="contact contact-online">
      <div class="contact-row">
        <svg viewBox="0 0 24 24" aria-hidden="true"><path d="M2 9l10-7 10 7v12H2zm2 1.5V19h16v-8.5l-8 5.5z"/></svg>
        <span>info@VYRLOTEN.com</span>
      </div>
      <div class="contact-row">
        <svg viewBox="0 0 24 24" aria-hidden="true"><path d="M12 2a10 10 0 1 0 0 20 10 10 0 0 0 0-20zm6.9 6h-3a15 15 0 0 0-1.3-3.9A8 8 0 0 1 18.9 8zM12 4c.8 1.2 1.5 2.5 1.9 4h-3.8c.4-1.5 1.1-2.8 1.9-4zM4.3 14a8 8 0 0 1 0-4h3.4a16 16 0 0 0 0 4zm.8 2h3a15 15 0 0 0 1.3 3.9A8 8 0 0 1 5.1 16zm3-8h-3a8 8 0 0 1 4.3-3.9A15 15 0 0 0 8.1 8zM12 20c-.8-1.2-1.5-2.5-1.9-4h3.8c-.4 1.5-1.1 2.8-1.9 4zm2.3-6H9.7a14 14 0 0 1 0-4h4.6a14 14 0 0 1 0 4zm.3 5.9a15 15 0 0 0 1.3-3.9h3a8 8 0 0 1-4.3 3.9zm1.7-5.9a16 16 0 0 0 0-4h3.4a8 8 0 0 1 0 4z"/></svg>
        <span>www.VYRLOTEN.com</span>
      </div>
    </div>
    <div class="footer-band"></div>
  </footer>
</main>
</body>
</html>
```